Business Card Design/Stationary Design

We would like designers to submit cool, hip business card designs (plus stationary designs) for a new, upstart software development company located in Toronto.
If you have any questions, please email us.
For inspiration on designs:
http://cardmuse.example/cool-business-cards/
http://layoutnotes.example/2008/05/36-cool-business-cards-you-should%E2%80%99ve-seen.html
http://gigharbor.example/general/18-smokin-hot-business-card-designs/

Card info:

Selvakumar (Selv) Nadarasan

Founder and CEO

47 Brindle Court, Suite 311

Toronto, ON M4K 2T8

Phone: 647-512-7730

Mobile: 416-273-5094

Fax: 647-512-7731

Email: selvakumar.nadarasan@mailbrook.example

www.quendrix.example
Updates

Hi everyone,

In terms of all the designs I have seen so far, here is what I like:

1.  I really like the "back" part of this design.  The "front" looks pretty decent as well, but for the "front", look at #2 on this list.  I like that.

http://www.pitchboard.example/image.aspx?imageLocation=1000_10001_2000_image.jpg&type=design300px&whiteLabelCustId=9999

2. "Side 1" of this I like, the front needs to be reworked.

http://www.pitchboard.example/image.aspx?imageLocation=1000_10002_2000_image.png&type=design300px&whiteLabelCustId=9999

3. http://www.pitchboard.example/image.aspx?imageLocation=1000_10003_2000_image.jpg&type=design300px&whiteLabelCustId=9999

4. http://www.pitchboard.example/image.aspx?imageLocation=1000_10004_2000_image.jpg&type=design300px&whiteLabelCustId=9999

Target Market(s)

We are focused on enterprise customers right now, so businesses with a long-term goal of also reaching out to the consumer market as well.

Industry/Entity Type

Software

Requirements
Must have
• Must look cool, ultra-modern, clean and eye-catching. Must incorporate our logo and the colors found in the logo.

```html
<!DOCTYPE html>
<html lang="en">
<head>
<meta charset="utf-8">
<title>Quendrix Business Card</title>
<link href="https://fonts.googleapis.com/css2?family=Source+Sans+3:wght@400;600&display=swap" rel="stylesheet">
<style>
  :root {
    --page: #ffffff;
    --card: #ffffff;
    --green: #3dff4a;
    --lime: #c4ff00;
    --lime-text: #d2f500;
    --olive: #86b800;
    --ink: #111111;
    --white: #ffffff;
  }
  html, body {
    margin: 0;
    padding: 0;
    width: 1200px;
    height: 846px;
    overflow: hidden;
    background: var(--page);
    font-family: "Source Sans 3", "Myriad Pro", sans-serif;
  }
  .sheet { position: relative; width: 1200px; height: 846px; }
  .card {
    position: absolute;
    top: 272px;
    width: 517px;
    height: 299px;
    background: var(--card);
    box-shadow: 0 0 24px rgba(0,0,0,0.10);
    overflow: hidden;
  }
  .card--front { left: 90px; }
  .card--back { left: 652px; }
  .card svg { position: absolute; inset: 0; display: block; }
  .brand { position: absolute; display: flex; align-items: center; }
  .brand__dot {
    border-radius: 50%;
    border: 7px solid var(--lime);
    box-sizing: border-box;
  }
  .brand__name {
    color: var(--ink);
    font-weight: 400;
    line-height: 1;
    letter-spacing: 0.5px;
  }
  .card--front .brand { left: 21px; top: 38px; gap: 15px; }
  .card--front .brand__dot { width: 56px; height: 56px; }
  .card--front .brand__name { font-size: 38px; }
  .card--back .brand { left: 126px; top: 87px; gap: 18px; }
  .card--back .brand__dot { width: 60px; height: 60px; }
  .card--back .brand__name { font-size: 40px; }

  .contact {
    position: absolute;
    right: 38px;
    top: 44px;
    text-align: right;
    color: var(--white);
    font-size: 15px;
    line-height: 19px;
    white-space: nowrap;
  }
  .contact p { margin: 0; }
  .contact__name { color: var(--lime-text); font-weight: 600; }
  .contact__title { margin-bottom: 19px !important; }
  .contact__address { margin-bottom: 8px !important; }
  .contact__label { color: var(--lime-text); font-weight: 600; }
  .contact__web { color: var(--lime-text); margin-top: 17px !important; margin-right: 3px !important; }

  .back-web {
    position: absolute;
    left: 0; right: 0;
    top: 251px;
    text-align: center;
    color: var(--white);
    font-size: 15px;
  }
</style>
</head>
<body>
<main class="sheet">
  <section class="card card--front">
    <svg viewBox="0 0 517 299" preserveAspectRatio="none" aria-hidden="true">
      <path fill="var(--olive)" d="M0,254 C100,238 180,195 240,130 L517,130 L517,299 L0,299 Z"/>
      <path fill="var(--lime)" d="M0,284 C110,252 205,175 255,90 L517,90 L517,299 L0,299 Z"/>
      <path fill="var(--green)" d="M277,0 L517,0 L517,299 L0,299 L0,291 C125,258 225,160 277,0 Z"/>
    </svg>
    <div class="brand">
      <span class="brand__dot"></span>
      <span class="brand__name">Quendrix</span>
    </div>
    <div class="contact">
      <p class="contact__name">Selvakumar (Selv) Nadarasan</p>
      <p class="contact__title">Founder and CEO</p>
      <p>47 Brindle Court, Suite 311</p>
      <p class="contact__address">Toronto, ON M4K 2T8</p>
      <p><span class="contact__label">P:</span> 647-512-7730</p>
      <p><span class="contact__label">M:</span> 416-273-5094</p>
      <p><span class="contact__label">F:</span> 647-512-7731</p>
      <p><span class="contact__label">E:</span> selvakumar.nadarasan@mailbrook.example</p>
      <p class="contact__web">www.quendrix.example</p>
    </div>
  </section>

  <section class="card card--back">
    <svg viewBox="0 0 517 299" preserveAspectRatio="none" aria-hidden="true">
      <path fill="var(--olive)" d="M170,226 C300,214 420,180 517,137 L517,299 L170,299 Z"/>
      <path fill="var(--lime)" d="M190,227 C330,220 440,196 517,161 L517,299 L190,299 Z"/>
      <path fill="var(--green)" d="M0,194 C60,212 130,226 220,228 C340,231 440,216 517,193 L517,299 L0,299 Z"/>
    </svg>
    <div class="brand">
      <span class="brand__dot"></span>
      <span class="brand__name">Quendrix</span>
    </div>
    <p class="back-web">www.quendrix.example</p>
  </section>
</main>
</body>
</html>
```